Director of a child care centre business card

Priscilla Hawthorne - Director/ Owner
418 Kestrel Rd
Fernleigh, 3168
Phone - 03 9184-6207
Fax - 03 91846218
info@tinyorchards.com.au
www.tinyorchards.com.au

Also needing another card same information but the name will be Megan Tolliver - Centre Director

```html
<!DOCTYPE html>
<html lang="en">
<head>
<meta charset="utf-8">
<title>Tiny Orchards – Business Cards</title>
<link rel="stylesheet" href="https://fonts.googleapis.com/css2?family=Quicksand:wght@400;500;600&display=swap">
<style>
  :root {
    --backdrop: #0c1a36;
    --card-navy: #1c2b8e;
    --frame-pink: #e834e8;
    --name-pink: #d63cd8;
    --text-magenta: #c42fc8;
    --title-grey: #8a5a94;
    --icon-green: #5cc43a;
    --paper: #ffffff;
    --divider-pink: #f2c4ef;
    --divider-blue: #b9cde0;
    --tagline: #e9e6ff;
  }
  * { margin: 0; padding: 0; box-sizing: border-box; }
  html, body {
    width: 1200px; height: 900px; overflow: hidden;
    background: var(--backdrop);
    font-family: "Quicksand", sans-serif;
  }
  .canvas { position: relative; width: 1200px; height: 900px; }

  /* Front of card */
  .card-front {
    position: absolute; left: 60px; top: 90px;
    width: 560px; height: 320px;
    background: var(--frame-pink);
    padding: 16px;
  }
  .card-front__field {
    width: 100%; height: 100%;
    background: var(--card-navy);
    display: flex; flex-direction: column;
    align-items: center; justify-content: center;
    gap: 10px;
  }
  .brand { display: flex; align-items: center; gap: 14px; }
  .brand__dot {
    width: 22px; height: 22px; border-radius: 50%;
    background: var(--frame-pink);
  }
  .brand__name {
    font-size: 44px; font-weight: 500;
    color: var(--frame-pink); letter-spacing: 1px;
  }
  .tagline {
    font-size: 17px; font-weight: 400;
    color: var(--tagline); letter-spacing: 1.5px;
  }

  /* Back of card */
  .card-back {
    position: absolute; left: 580px; top: 490px;
    width: 560px; height: 320px;
    background: var(--paper);
    border-bottom: 6px solid var(--frame-pink);
  }
  .divider {
    position: absolute; left: 282px; top: 28px;
    width: 3px; height: 270px;
    background: linear-gradient(var(--divider-pink) 0 48%, var(--divider-blue) 48% 100%);
  }
  .holder {
    position: absolute; left: 30px; top: 140px;
    width: 240px;
  }
  .holder__name {
    font-size: 22px; font-weight: 600;
    color: var(--name-pink); white-space: nowrap;
  }
  .holder__title {
    font-size: 10px; font-weight: 500;
    color: var(--title-grey); margin-left: 48px;
  }
  .mini-mark {
    position: absolute; right: 40px; top: 28px;
    width: 110px; height: 90px;
    background: var(--card-navy);
    display: flex; align-items: center; justify-content: center;
  }
  .mini-mark__name {
    font-size: 14px; font-weight: 500; color: var(--frame-pink);
  }
  .contact {
    position: absolute; right: 26px; top: 158px;
    list-style: none;
    display: flex; flex-direction: column; gap: 7px;
    align-items: flex-end;
  }
  .contact__item {
    display: flex; align-items: center; gap: 6px;
    font-size: 12px; font-weight: 500; color: var(--text-magenta);
  }
  .contact__icon { width: 13px; height: 13px; fill: var(--icon-green); }
</style>
</head>
<body>
<main class="canvas">

  <section class="card-front" aria-label="Card front">
    <div class="card-front__field">
      <div class="brand">
        <span class="brand__dot"></span>
        <span class="brand__name">Tiny Orchards</span>
      </div>
      <p class="tagline">Child Care And Kinder</p>
    </div>
  </section>

  <section class="card-back" aria-label="Card back">
    <div class="holder">
      <p class="holder__name">Priscilla Hawthorne</p>
      <p class="holder__title">Director/ Owner</p>
    </div>
    <div class="divider"></div>
    <div class="mini-mark"><span class="mini-mark__name">Tiny Orchards</span></div>
    <ul class="contact">
      <li class="contact__item">03 9184-6207
        <svg class="contact__icon" viewBox="0 0 16 16"><path d="M3 1l3 3-2 2c1 2 3 4 5 5l2-2 3 3-2 2C7 14 2 9 1 3z"/></svg>
      </li>
      <li class="contact__item">03 91846218
        <svg class="contact__icon" viewBox="0 0 16 16"><path d="M4 1h8v4H4zM1 6h14v6h-3v3H4v-3H1zM5 10v4h6v-4z"/></svg>
      </li>
      <li class="contact__item">info@tinyorchards.com.au
        <svg class="contact__icon" viewBox="0 0 16 16"><path d="M1 3h14v10H1zM2 4l6 5 6-5z" fill-rule="evenodd"/></svg>
      </li>
      <li class="contact__item">www.tinyorchards.com.au
        <svg class="contact__icon" viewBox="0 0 16 16"><circle cx="8" cy="8" r="7"/></svg>
      </li>
      <li class="contact__item">418 Kestrel Rd Fernleigh, 3168
        <svg class="contact__icon" viewBox="0 0 16 16"><path d="M8 1a5 5 0 0 1 5 5c0 4-5 9-5 9S3 10 3 6a5 5 0 0 1 5-5z"/></svg>
      </li>
    </ul>
  </section>

</main>
</body>
</html>
```